Graphic design of labels for scented candles

Following a change in our team structure, a deadline was put in place and the brief changed.
We need a beautiful label for our candles, one that sticks *all around the glass*. Must obviously include our logo as well as the description of the perfume.
The clientele is mainly female, between 35 and 65 years old, of a classic nature.
Brand values:
Feminine
Warm-joyful
Sophisticated-elegant
Eco-friendly, pet-friendly
Natural
Inspires confidence.
The idea is to have something different, the final appearance must be elegant and refined, which will be your challenge given the shape.

What we need:
- changeable colors
- small transparent elements which can be printed on a gold or silver paper background (example: logo, frame, elements, etc.)

- the logo (black or very dark gray) must be present + text "vegetable candle", then the perfume and below:
vegetable wax - handcrafted"
I am attaching a picture of our current labels to the files.
For the size I'll let you manage.
These labels can also be assigned to derived products such as room fragrances, pillow mists, etc.
The brand targets the middle class and above.
For the fonts I leave the choice to you.
Thank you and good luck to all !

Update: there is no longer a cat's head as a background shape, you have free choice.
THANKS

Target Market(s)

Women aged 35 to 65

Industry/Entity Type

Industrie du Parfum

Colors
00AB8E
00BBA5
67D7C9
C6EFE9
E9F9F6
59FF00
82FF00
B8FF75
E3FFCB
F4FFEA
FFF300
FFF600
FEFA6F
FFFEC7
FFFEE8
FFC000
F8CF3A
FAE287
FDF2CF
FEFAEE
F0912C
F2A743
F7CA91
FBE8D2
FDF5EE
EE7325
F08F49
F5BC92
FAE3D3
FDF4ED
EB3D1F
EC4F4E
F09395
F8D3D4
FCEDEE
E54698
E96AAD
F1A4CE
F9D9EA
FCEFF6
A7469A
B969AE
D3A5CF
EDDBEB
F8F0F9
6B429C
8869AF
B7A5CE
E3DAEB
F3F0F8

Requirements
Must have
• modifiable colors - small transparent elements which can be printed on a gold or silver paper background (example: frame, elements, etc.) - the logo (black or very dark gray) must be present + text "vegetable candle, then the perfume and below: vegetable wax - handcrafted"
Nice to have
• Elements that could be made transparent (logo text frame) to be able to edit on gold papers and give a luxurious appearance
Should not have
• no childish appearance.

```html
<!DOCTYPE html>
<html lang="en">
<head>
<meta charset="utf-8">
<title>Lumelle Candle – label series</title>
<link rel="stylesheet" href="https://fonts.googleapis.com/css2?family=Montserrat:wght@300;400;500&family=Mrs+Saint+Delafield&display=swap">
<style>
  :root {
    --paper: #ffffff;
    --ink: #111111;
    --gold-dark: #9a7a45;
    --gold-mid: #c9a96e;
    --gold-light: #f5ecc8;
    --gold-solid: #b08d57;
    --cream: #f7ead8;
    --cream-ink: #8a7158;
    --night: #000000;
    --swiss-red: #d52b1e;
    --gold-sheen: linear-gradient(90deg, var(--gold-dark) 0%, var(--gold-mid) 42%, var(--gold-light) 74%, #c8ad72 100%);
  }
  * { box-sizing: border-box; margin: 0; padding: 0; }
  html, body { width: 1200px; height: 948px; overflow: hidden; background: var(--paper); }
  body { position: relative; font-family: "Montserrat", sans-serif; color: var(--ink); }

  .label-base { position: absolute; }
  .label-base--gold-square { left: 72px; top: 113px; width: 292px; height: 274px; background: var(--gold-sheen); }
  .label-base--gold-round { left: 423px; top: 99px; width: 330px; height: 330px; border-radius: 50%; background: var(--gold-sheen); }
  .label-base--floral { left: 792px; top: 93px; width: 332px; height: 332px; border-radius: 50%;
    background: radial-gradient(circle, var(--cream) 55%, #e9d6bd 100%); }
  .label-base--black-pill { left: 76px; top: 477px; width: 274px; height: 379px; border-radius: 137px; background: var(--night); }
  .label-base--gold-wide { left: 405px; top: 549px; width: 319px; height: 274px; background: var(--gold-sheen); }

  .panel {
    position: absolute; background: var(--paper);
    display: flex; flex-direction: column; align-items: center;
    border-radius: 52px 38px 78px 0;
  }
  .panel--a { left: 118px; top: 158px; width: 190px; height: 210px; }
  .panel--b { left: 486px; top: 166px; width: 190px; height: 211px; }
  .panel--c { left: 863px; top: 158px; width: 194px; height: 218px; border-radius: 44px 30px 70px 0; }
  .panel--d { left: 117px; top: 559px; width: 190px; height: 210px; }
  .panel--e { left: 439px; top: 594px; width: 249px; height: 213px; border-radius: 6px; }

  .brand-name { margin-top: 22px; font-weight: 500; font-size: 27px; letter-spacing: 1px; line-height: 1; color: var(--ink); }
  .brand-name--gold { color: var(--gold-solid); }
  .brand-line { margin-top: 6px; display: flex; align-items: center; gap: 4px; font-size: 9px; letter-spacing: 4px; font-weight: 400; }
  .brand-line::before, .brand-line::after { content: ""; width: 14px; height: 1px; background: var(--ink); }
  .brand-web { margin-top: 1px; font-size: 4.5px; letter-spacing: 1px; }
  .swiss-mark { margin-top: 3px; width: 6px; height: 6px; background: var(--swiss-red); }
  .product-type { margin-top: 6px; font-size: 8.5px; font-weight: 300; letter-spacing: 0.2px; }
  .scent { margin-top: 20px; font-family: "Mrs Saint Delafield", cursive; font-size: 40px; line-height: 1; white-space: nowrap; }
  .material { position: absolute; left: 14px; bottom: 8px; font-size: 7px; font-weight: 400; }

  .panel--e .brand-name { margin-top: 24px; font-size: 30px; }
  .panel--e .scent { margin-top: 10px; font-size: 46px; }
  .panel--e .material { left: 82px; bottom: 14px; }
</style>
</head>
<body>

  <div class="label-base label-base--gold-square"></div>
  <div class="panel panel--a">
    <div class="brand-name brand-name--gold">Lumelle</div>
    <div class="brand-line">CANDLE</div>
    <div class="brand-web">lumelle candle com</div>
    <div class="swiss-mark"></div>
    <div class="product-type">VEGETABLE CANDLE</div>
    <div class="scent">Cannelle douce</div>
    <div class="material">vegetable wax - handcrafted</div>
  </div>

  <div class="label-base label-base--gold-round"></div>
  <div class="panel panel--b">
    <div class="brand-name brand-name--gold">Lumelle</div>
    <div class="brand-line">CANDLE</div>
    <div class="brand-web">lumelle candle com</div>
    <div class="swiss-mark"></div>
    <div class="product-type">VEGETABLE CANDLE</div>
    <div class="scent">Cannelle douce</div>
    <div class="material">vegetable wax - handcrafted</div>
  </div>

  <div class="label-base label-base--floral" role="img" aria-label="Hand-drawn floral pattern in dark brown on cream"></div>
  <div class="panel panel--c">
    <div class="brand-name">Lumelle</div>
    <div class="brand-line">CANDLE</div>
    <div class="brand-web">lumelle candle com</div>
    <div class="swiss-mark"></div>
    <div class="product-type">VEGETABLE CANDLE</div>
    <div class="scent">Cannelle douce</div>
    <div class="material">vegetable wax - handcrafted</div>
  </div>

  <div class="label-base label-base--black-pill"></div>
  <div class="panel panel--d">
    <div class="brand-name">Lumelle</div>
    <div class="brand-line">CANDLE</div>
    <div class="brand-web">lumelle candle com</div>
    <div class="swiss-mark"></div>
    <div class="product-type">VEGETABLE CANDLE</div>
    <div class="scent">Cannelle douce</div>
    <div class="material">vegetable wax - handcrafted</div>
  </div>

  <div class="label-base label-base--gold-wide"></div>
  <div class="panel panel--e">
    <div class="brand-name">Lumelle</div>
    <div class="brand-line">CANDLE</div>
    <div class="brand-web">lumelle candle com</div>
    <div class="swiss-mark"></div>
    <div class="product-type">VEGETABLE CANDLE</div>
    <div class="scent">Cannelle douce</div>
    <div class="material">vegetable wax - handcrafted</div>
  </div>

</body>
</html>
```